** Wanted ** Wordpress web design for scaffolding rental and construction company

We need a website design and must be functional to show a basic overview of what our company offers as a service. We have a domain name and a logo but we need web design. This web site should have another scaffolding rental page for construction and renovation as well as a quote section where customers can enter their personal information and also upload photos. The site% 26quot; www.brixmorvo.com% 26quot; should be intuitive, clear and classy ... The logo must be found on the site in several ways.

Target Market(s)

Professional and no professional

Coding

Coded - Design and coding required

Number of Pages Required

3 page

Font styles to use
Serif
Sans Serif
Decorative
Script

Requirements
Must have
• Our logo
Nice to have
• Slogan:% 26quot; The height% 26 # 224; port% 26 # 233; e hand% 26quot;

```html
<!DOCTYPE html>
<html lang="en">
<head>
<meta charset="utf-8">
<title>Brixmorvo — Equipment &amp; Scaffolding</title>
<link href="https://fonts.googleapis.com/css2?family=Oswald:wght@500;600&family=Poppins:wght@400;500;600&display=swap" rel="stylesheet">
<style>
:root{
  --orange:#f0821e;
  --ink:#222;
  --text:#555;
  --muted:#888;
  --dark:#1c1c1c;
  --black:#000;
  --light:#f3f3f3;
  --white:#fff;
}
*{box-sizing:border-box;margin:0;padding:0}
html,body{width:1200px;height:2806px;overflow:hidden}
body{position:relative;background:var(--white);font-family:'Poppins',sans-serif;color:var(--text)}
.abs{position:absolute}
.head{font-family:'Oswald',sans-serif;font-weight:600;text-transform:uppercase;letter-spacing:.2px}
.hl{color:var(--orange)}
.brand{display:flex;align-items:center;gap:10px;font-family:'Poppins',sans-serif;font-weight:600;font-size:22px;color:var(--orange);letter-spacing:1px}
.brand i{display:block;width:22px;height:22px;background:var(--orange)}

/* hero */
.hero{left:0;top:0;width:1200px;height:494px;background:linear-gradient(120deg,#3b342e 0%,#6b5845 35%,#4a4036 65%,#2e2a27 100%)}
.hero-shade{left:0;top:0;width:1200px;height:494px;background:linear-gradient(90deg,rgba(0,0,0,.35),rgba(0,0,0,.05) 50%,rgba(0,0,0,.3))}
.nav{top:58px;display:flex;gap:0;left:512px}
.nav a{font-family:'Oswald',sans-serif;font-weight:500;font-size:14px;color:#fff;text-decoration:none;text-transform:uppercase;margin-right:34px}
.phone-btn{left:890px;top:47px;width:153px;height:38px;border-radius:19px;background:var(--orange);display:flex;align-items:center;justify-content:center;gap:10px;font-family:'Oswald',sans-serif;font-weight:500;font-size:18px;color:#fff}
.hero-title{left:153px;top:203px;font-size:56px;line-height:58px;color:#fff}
.hero-sub{left:155px;top:338px;font-size:15px;color:#fff}
.enquire{left:808px;top:174px;width:236px;height:310px;border:1px solid rgba(255,255,255,.7);border-radius:4px;background:rgba(0,0,0,.72);padding:18px 24px}
.enquire h3{font-size:20px;color:var(--orange)}
.enquire p{font-size:11px;color:#fff;margin:2px 0 20px}
.field{height:36px;border:1px solid rgba(255,255,255,.5);border-radius:5px;font-size:11px;color:#fff;padding:9px 13px;margin-bottom:13px}
.field.tall{height:52px}
.btn{background:var(--orange);color:#fff;font-family:'Oswald',sans-serif;font-weight:500;text-transform:uppercase;text-align:center}
.enquire .btn{height:36px;line-height:36px;border-radius:4px;font-size:14px;margin-top:2px}
.dots-v{left:1130px;top:240px}
.dots-v span{display:block;width:8px;height:8px;border-radius:50%;background:#fff;margin:0 auto 16px}
.dots-v span.on{width:14px;height:14px;border:2px solid #fff;background:var(--orange);margin-bottom:12px}

/* about */
.about-text{left:615px;top:632px;width:430px}
.about-text h2{font-size:28px;color:var(--ink)}
.about-text h4{font-size:14px;font-weight:600;color:var(--ink);margin:14px 0 16px}
.about-text p{font-size:13px;line-height:28px;margin-bottom:14px}
.pill{border-radius:17px;height:33px;line-height:33px;font-size:14px}

/* equipment */
.equip-title{left:0;width:1200px;top:1098px;text-align:center;font-size:27px;color:#fff}
.card{top:1177px;width:207px;height:286px;background:#fff;border:1px solid #ddd}
.card .ph{position:absolute;left:20px;top:22px;width:165px;height:170px;border-radius:4px}
.card .lbl{position:absolute;left:20px;top:236px;display:flex;align-items:center;gap:10px;font-size:13px;font-weight:500;color:var(--ink)}
.card .lbl i{display:block;width:18px;height:18px;border:2px solid var(--orange);border-radius:2px}
.arrow{width:26px;height:26px;border-radius:50%;background:var(--orange);color:#fff;display:flex;align-items:center;justify-content:center}

/* projects */
.sec-title{left:0;width:1200px;text-align:center;font-size:28px;color:var(--ink)}
.sec-sub{left:0;width:1200px;text-align:center;font-size:13px}
.project-panel{left:763px;top:1649px;width:281px;height:292px;background:var(--light);padding:30px 28px}
.project-panel h4{font-size:15px;font-weight:600;color:#333;line-height:24px}
.project-panel p{font-size:13px;line-height:24px;margin:12px 0 18px}
.project-panel .pill{width:146px;font-family:'Poppins',sans-serif;font-weight:600;font-size:12px}
.dots-h{display:flex;gap:10px;align-items:center}
.dots-h span{width:8px;height:8px;border-radius:50%;border:1px solid #999}
.dots-h span.on{background:var(--orange);border-color:var(--orange)}

/* testimonials */
.customers{left:0;top:2020px;width:1200px;height:443px;background:var(--light)}
.quote{top:2161px;width:282px;height:207px;background:#fff;box-shadow:0 2px 8px rgba(0,0,0,.06);padding:22px 20px}
.quote h5{font-size:15px;font-weight:600;color:var(--ink)}
.quote small{display:block;font-size:11px;color:var(--muted);margin-top:2px}
.quote .avatar{position:absolute;right:34px;top:20px;width:44px;height:44px;border-radius:50%;background:linear-gradient(135deg,#b9a08c,#5b4a40)}
.quote hr{border:0;border-top:1px solid #e5e5e5;margin:16px 0 14px}
.quote p{font-size:12.5px;line-height:21px}
.dots-plain span{border:0;background:#c9c9c9}

/* footer */
.footer-col{top:2584px}
.footer-col h6{font-family:'Poppins',sans-serif;font-weight:600;font-size:14px;color:var(--orange);text-transform:uppercase;border-bottom:1px solid var(--orange);display:inline-block;margin-bottom:14px}
.footer-col a{display:block;font-size:13px;color:#ccc;text-decoration:none;line-height:28.5px}
.copy{left:151px;top:2673px;font-size:11px;line-height:18px;color:#ccc}
.connect{left:841px;width:142px;height:37px;border:1px solid #ddd;display:flex;align-items:center;gap:10px;padding-left:16px;font-size:12px;font-weight:500;color:#fff}
.connect i{display:block;width:13px;height:13px;background:var(--orange)}
</style>
</head>
<body>

<!-- Hero -->
<div class="abs hero" role="img" aria-label="Photo of workers on orange scissor lifts inside a steel-framed building"></div>
<div class="abs hero-shade"></div>
<div class="abs brand" style="left:160px;top:64px">BRIXMORVO<i></i></div>
<nav class="abs nav">
  <a href="#">Home</a><a href="#">Services</a><a href="#">Projects</a><a href="#">About</a><a href="#">Contact</a>
</nav>
<div class="abs phone-btn">
  <svg width="18" height="18" viewBox="0 0 24 24" fill="none" stroke="#fff" stroke-width="1.8"><path d="M5 3h4l2 5-2.5 1.5a11 11 0 0 0 6 6L16 13l5 2v4a2 2 0 0 1-2 2A16 16 0 0 1 3 5a2 2 0 0 1 2-2z"/></svg>
  03 5550 1847
</div>
<h1 class="abs head hero-title">Manage your<br>equipment</h1>
<p class="abs hero-sub">The simple way to record and produce your next hit</p>
<form class="abs enquire">
  <h3 class="head">Enquire now</h3>
  <p>We will call you back right back!</p>
  <div class="field">Full Name</div>
  <div class="field">Phone Number</div>
  <div class="field tall">Message</div>
  <div class="btn">Send message</div>
</form>
<div class="abs dots-v"><span class="on"></span><span></span><span></span><span></span></div>
<svg class="abs" style="left:0;top:494px" width="1200" height="44"><polygon points="0,0 605,0 650,43 1200,43 1200,0" fill="#fff"/><polygon points="605,0 1200,0 1200,43 650,43" fill="#f0821e"/><rect x="0" y="-1" width="606" height="2" fill="#fff"/></svg>

<!-- About -->
<svg class="abs" style="left:87px;top:572px" width="510" height="390" role="img" aria-label="Construction workers with scaffolding and machinery photos in diamond frames">
  <g fill="#bbb"><circle cx="30" cy="150" r="1.6"/><circle cx="60" cy="120" r="1.6"/><circle cx="90" cy="90" r="1.6"/><circle cx="120" cy="60" r="1.6"/><circle cx="150" cy="30" r="1.6"/><circle cx="30" cy="180" r="1.6"/><circle cx="60" cy="210" r="1.6"/><circle cx="90" cy="240" r="1.6"/><circle cx="120" cy="270" r="1.6"/><circle cx="150" cy="300" r="1.6"/><circle cx="180" cy="330" r="1.6"/><circle cx="45" cy="165" r="1.6"/><circle cx="75" cy="105" r="1.6"/><circle cx="105" cy="255" r="1.6"/><circle cx="165" cy="345" r="1.6"/></g>
  <defs><linearGradient id="g1" x1="0" y1="0" x2="1" y2="1"><stop offset="0" stop-color="#7d8a92"/><stop offset=".6" stop-color="#4c5358"/><stop offset="1" stop-color="#2f3336"/></linearGradient><linearGradient id="g2" x1="0" y1="0" x2="1" y2="1"><stop offset="0" stop-color="#8a3a30"/><stop offset="1" stop-color="#2d2a2a"/></linearGradient></defs>
  <polygon points="238,2 444,190 238,386 44,194" fill="url(#g1)"/>
  <polygon points="403,97 500,194 403,291 306,194" fill="#fff"/>
  <polygon points="403,97 500,194 403,291 306,194" fill="url(#g2)" transform="translate(403 194) scale(.94) translate(-403 -194)"/>
</svg>
<div class="abs about-text">
  <h2 class="head">About <span class="hl">Brixmorvo</span></h2>
  <h4>Your Concrete Formwork and Scaffolding Company</h4>
  <p>We’re a leading manufacturer and supplier of formwork, shoring and temporary scaffolding systems, providing high performance engineered products and reliable services.</p>
  <p>Lorem ipsum dolor sit amet, consectetur adipiscing elit. Ut felis dui, facilisis ornare elit in, ultrices tempus magna. Praesent vulputate ultricies neque, ut aliquet nulla dignissim quis</p>
</div>
<div class="abs btn pill" style="left:615px;top:917px;width:138px">Learn more</div>

<!-- Equipment -->
<div class="abs" style="left:0;top:997px;width:1200px;height:324px;background:linear-gradient(90deg,#2a2f36,#3a3f44 50%,#2b2e33)" role="img" aria-label="Dark warehouse photo with stacked equipment"></div>
<div class="abs" style="left:0;top:997px;width:1200px;height:324px;background:rgba(0,0,0,.45)"></div>
<svg class="abs" style="left:0;top:996px" width="1200" height="48"><polygon points="0,0 605,0 555,46 0,46" fill="#fff"/><rect x="0" y="36" width="565" height="11" fill="#f0821e"/><polygon points="565,36 555,47 565,47" fill="#f0821e"/></svg>
<h2 class="abs head equip-title">Popular equipment types</h2>
<div class="abs arrow" style="left:82px;top:1308px"><svg width="10" height="10" viewBox="0 0 10 10"><path d="M6.5 1.5L3 5l3.5 3.5" stroke="#fff" stroke-width="1.6" fill="none"/></svg></div>
<div class="abs arrow" style="left:1078px;top:1308px"><svg width="10" height="10" viewBox="0 0 10 10"><path d="M3.5 1.5L7 5 3.5 8.5" stroke="#fff" stroke-width="1.6" fill="none"/></svg></div>
<div class="abs card" style="left:154px"><div class="ph" role="img" aria-label="Orange telescopic reach forklift" style="background:linear-gradient(160deg,#fff,#f3d2b8 50%,#fff)"></div><div class="lbl"><i></i>Reach Forklifts &nbsp;→</div></div>
<div class="abs card" style="left:383px"><div class="ph" role="img" aria-label="Blue and white scissor lift" style="background:linear-gradient(160deg,#fff,#cfdbe8 50%,#fff)"></div><div class="lbl"><i></i>Scissor Lifts &nbsp;→</div></div>
<div class="abs card" style="left:611px"><div class="ph" role="img" aria-label="Blue articulated boom lift" style="background:linear-gradient(160deg,#fff,#c7dbee 50%,#fff)"></div><div class="lbl"><i></i>Boom Lifts &nbsp;→</div></div>
<div class="abs card" style="left:839px"><div class="ph" role="img" aria-label="Towable light tower trailer" style="background:linear-gradient(160deg,#fff,#dedede 50%,#fff)"></div><div class="lbl"><i></i>Towable Light Rowers &nbsp;→</div></div>

<!-- Projects -->
<h2 class="abs head sec-title" style="top:1508px">Our <span class="hl">recent projects</span></h2>
<p class="abs sec-sub" style="top:1555px">Lorem ipsum dolor sit amet, consectetur adipiscing elit. Ut felis dui,</p>
<div class="abs" style="left:155px;top:1619px;width:813px;height:349px;background:linear-gradient(180deg,#9aa3a8 0%,#8a8a78 35%,#5f6650 70%,#6d6a5c 100%)" role="img" aria-label="Aerial photo of a refinery under construction with scaffolding towers"></div>
<div class="abs project-panel">
  <h4>First step in the modernisation for NORVALTA</h4>
  <p>Lorem ipsum dolor sit amet, consectetur adipiscing elit. Ut felis dui, facilisis ornare elit in, ultrices tempus magna.</p>
  <div class="btn pill">Show projects</div>
  <div class="dots-h" style="margin:18px 0 0 12px"><span></span><span class="on"></span><span></span></div>
</div>

<!-- Customers -->
<div class="abs customers"></div>
<h2 class="abs head sec-title" style="top:2077px">Our <span class="hl">customers say</span></h2>
<div class="abs quote" style="left:155px"><h5>Mara Quell</h5><small>Vise Business Analyst</small><div class="avatar" role="img" aria-label="Customer portrait"></div><hr><p>Lorem ipsum dolor sit amet, consectetur adipiscing elit, sed do eiusmod tempor incididunt ut labore et dolore magna aliqua. Ut enim ad</p></div>
<div class="abs quote" style="left:459px"><h5>Mara Quell</h5><small>Vise Business Analyst</small><div class="avatar" role="img" aria-label="Customer portrait"></div><hr><p>Lorem ipsum dolor sit amet, consectetur adipiscing elit, sed do eiusmod tempor incididunt ut labore et dolore magna aliqua. Ut enim ad</p></div>
<div class="abs quote" style="left:763px"><h5>Mara Quell</h5><small>Vise Business Analyst</small><div class="avatar" role="img" aria-label="Customer portrait"></div><hr><p>Lorem ipsum dolor sit amet, consectetur adipiscing elit, sed do eiusmod tempor incididunt ut labore et dolore magna aliqua. Ut enim ad</p></div>
<div class="abs dots-h dots-plain" style="left:572px;top:2409px;gap:16px"><span></span><span class="on"></span><span></span></div>

<!-- Footer -->
<svg class="abs" style="left:0;top:2462px" width="1200" height="344"><rect x="0" y="0" width="1200" height="344" fill="#000"/><polygon points="0,0 605,0 555,47 0,47" fill="#f3f3f3"/><rect x="0" y="36" width="565" height="11" fill="#f0821e"/><polygon points="565,36 555,47 565,47" fill="#f0821e"/></svg>
<div class="abs brand" style="left:160px;top:2590px">BRIXMORVO<i></i></div>
<p class="abs copy">Copyright © 2020 BRIXMORVO.<br>All Rights Reserved</p>
<div class="abs footer-col" style="left:374px"><h6>Browse</h6><a href="#">Home</a><a href="#">Workplaces</a><a href="#">Chargers</a><a href="#">car Brands</a><a href="#">Regions</a></div>
<div class="abs footer-col" style="left:529px"><h6>About us</h6><a href="#">News</a><a href="#">Gallery</a><a href="#">About us</a><a href="#">Contact us</a></div>
<div class="abs footer-col" style="left:685px"><h6>Head office</h6><a>Hollin House</a><a>Drayfield Road</a><a>Amberton</a><a>Westmere</a><a>AB12 3CD</a></div>
<div class="abs footer-col" style="left:841px"><h6>Connect</h6></div>
<div class="abs connect" style="top:2618px">
  <svg width="15" height="15" viewBox="0 0 24 24" fill="none" stroke="#fff" stroke-width="1.8"><path d="M5 3h4l2 5-2.5 1.5a11 11 0 0 0 6 6L16 13l5 2v4a2 2 0 0 1-2 2A16 16 0 0 1 3 5a2 2 0 0 1 2-2z"/></svg>
  <span style="font-weight:400;font-size:13px">01632 960 418</span></div>
<div class="abs connect" style="top:2666px">
  <svg width="15" height="11" viewBox="0 0 15 11"><rect width="15" height="11" fill="#f0821e"/><path d="M0 0l7.5 6L15 0" stroke="#000" stroke-width="1.2" fill="none"/></svg>
  SEND AN EMAIL</div>
<div class="abs connect" style="top:2712px"><i></i>FOLLOW US</div>

</body>
</html>
```